washable paper bags and accessories

We are three sisters who have discovered a mutual love of bags made from washable paper. It is a brand new business venture for bags, handbags, cosmetic bags, and home storage solutions and décor all made with washable paper.
We would like to have white crumpled paper as a background for both sides. Front of card with the words "plume douce cloth" only in "Wanderlust Keystroke Regular" font. Back of card with appointment style format for our next pop up stall
Target Market(s)
mums, females
Industry/Entity Type
Business
Contact Information for Business Card
ph: 0487215364
email:plumedoucecloth@mailbarrow.com

```html
<!DOCTYPE html>
<html lang="en">
<head>
<meta charset="utf-8">
<title>Plume Douce Cloth – Business Card</title>
<link rel="stylesheet" href="https://fonts.googleapis.com/css2?family=Lobster&family=Roboto:wght@400;500&family=Cutive&display=swap">
<style>
  :root {
    --brand-red: #dd0a0a;
    --ink: #1b1b1b;
    --paper: #fbfbfa;
    --paper-shade: #efefed;
    --backdrop: #eeeeee;
    --white: #ffffff;
  }
  html, body {
    margin: 0;
    width: 1200px;
    height: 993px;
    overflow: hidden;
    background: var(--backdrop);
  }
  .canvas {
    position: relative;
    width: 1200px;
    height: 993px;
  }
  .card {
    position: absolute;
    top: 342px;
    width: 540px;
    height: 309px;
    background: radial-gradient(circle at 30% 30%, var(--paper) 0%, var(--paper-shade) 100%);
    box-shadow: 0 6px 18px rgba(0,0,0,0.12);
    overflow: hidden;
  }
  .card--appointment { left: 40px; }
  .card--brand { left: 620px; }

  /* Appointment side */
  .appointment__band {
    height: 72px;
    margin-top: 14px;
    background: var(--brand-red);
    display: flex;
    align-items: center;
    justify-content: center;
  }
  .appointment__title {
    font-family: "Lobster", cursive;
    font-size: 38px;
    color: var(--white);
    margin: 0;
    font-weight: 400;
  }
  .appointment__fields {
    padding: 22px 30px 0 40px;
  }
  .field {
    display: flex;
    align-items: flex-end;
    height: 52px;
    font-family: "Roboto", sans-serif;
    font-size: 17px;
    font-weight: 500;
    color: var(--ink);
  }
  .field__line {
    flex: 1;
    border-bottom: 2px solid var(--ink);
    margin-left: 2px;
    margin-bottom: 3px;
  }
  .field__suffix {
    font-size: 15px;
    margin-bottom: 4px;
  }

  /* Brand side */
  .brand__message {
    text-align: center;
    padding-top: 58px;
  }
  .brand__name,
  .brand__font {
    font-family: "Lobster", cursive;
    color: var(--brand-red);
    font-size: 32px;
    margin: 0;
    line-height: 1.15;
  }
  .brand__joiner {
    font-family: "Cutive", serif;
    font-size: 19px;
    color: var(--ink);
    margin: 4px 0 6px;
  }
  .brand__contact {
    position: absolute;
    left: 0;
    right: 0;
    bottom: 14px;
    height: 64px;
    background: var(--brand-red);
    display: flex;
    align-items: center;
    justify-content: center;
    gap: 10px;
    font-family: "Roboto", sans-serif;
    font-size: 17px;
    color: var(--white);
  }
  .contact-item {
    display: flex;
    align-items: center;
    gap: 6px;
  }
  .contact-item svg { width: 20px; height: 20px; }
</style>
</head>
<body>
<main class="canvas">

  <section class="card card--appointment" aria-label="Appointment side">
    <div class="appointment__band">
      <h2 class="appointment__title">Appointment</h2>
    </div>
    <div class="appointment__fields">
      <div class="field"><span>Name:</span><span class="field__line"></span></div>
      <div class="field"><span>at:</span><span class="field__line"></span><span class="field__suffix">A.M/P.M</span></div>
      <div class="field"><span>on:</span><span class="field__line"></span></div>
    </div>
  </section>

  <section class="card card--brand" aria-label="Brand side">
    <div class="brand__message">
      <p class="brand__name">“Plume Douce Cloth”</p>
      <p class="brand__joiner">only in</p>
      <p class="brand__font">“Wanderlust Keystroke Regular”</p>
    </div>
    <div class="brand__contact">
      <span class="contact-item">
        <svg viewBox="0 0 20 20" aria-hidden="true">
          <circle cx="10" cy="10" r="10" fill="#ffffff"/>
          <path d="M7 5.5c.6-.4 1.2-.3 1.5.3l.8 1.6c.2.5.1 1-.3 1.3l-.6.5c.5 1.1 1.3 1.9 2.4 2.4l.5-.6c.3-.4.8-.5 1.3-.3l1.6.8c.6.3.7.9.3 1.5-.7 1-1.8 1.4-3 .9-2.3-.9-4-2.6-4.9-4.9-.5-1.2-.1-2.3.4-3.5z" fill="#dd0a0a"/>
        </svg>
        0487215364
      </span>
      <span class="contact-item">
        <svg viewBox="0 0 20 20" aria-hidden="true">
          <circle cx="10" cy="10" r="9" fill="none" stroke="#ffffff" stroke-width="1.6"/>
          <rect x="5" y="6.5" width="10" height="7" fill="none" stroke="#ffffff" stroke-width="1.3"/>
          <path d="M5 6.5l5 4 5-4" fill="none" stroke="#ffffff" stroke-width="1.3"/>
        </svg>
        plumedoucecloth@mailbarrow.com
      </span>
    </div>
  </section>

</main>
</body>
</html>
```